Lorn Systems

Looking for a web site design to market our services/applications
We write and supply bespoke web applications for the offshore and construction industries
Our initial product is Velk - rope access equipment management
Our buyers will be Rope Access companies via trade associations such as OBWEN and KLUDE
we have a logo designed see it attached we would like to see crisp professional designs based around these colours and design
we will supply web copy later
looking for home, services, blog, contact us, order and a general template (privacy, site map, T&C) pages
Updates
This payment will be for the homepage only
We can discuss other options (pages) with the successful designer
Regards
Brian
Industry/Entity Type
Construction
Look and feel
Each slider illustrates characteristics of the customer's brand and the style your logo design should communicate.

```html
<!DOCTYPE html>
<html lang="en">
<head>
<meta charset="utf-8">
<title>Lorn Systems</title>
<link rel="stylesheet" href="https://fonts.googleapis.com/css2?family=Nunito+Sans:wght@400;600&family=Source+Sans+3:ital,wght@0,400;0,600;1,400&display=swap">
<style>
:root{
  --blue:#2d6fb5;
  --blue-bright:#5b9be0;
  --navy:#1b3a78;
  --text:#555;
  --heading:#444;
  --band:#f6f6f6;
  --footer:#3b3b3b;
  --date:#b9b9b9;
  --white:#fff;
}
*{margin:0;padding:0;box-sizing:border-box}
html,body{width:979px;height:1200px;overflow:hidden;background:var(--white)}
body{position:relative;font-family:"Source Sans 3",sans-serif;color:var(--text)}
.abs{position:absolute}

.site-header{left:0;top:0;width:979px;height:78px;background:var(--white)}
.brand{left:106px;top:20px;display:flex;align-items:center;gap:8px}
.brand-mark{width:36px;height:36px;background:#e8ecf3;border-radius:4px}
.brand-name{font-family:"Nunito Sans",sans-serif;font-weight:600;font-size:17px;color:var(--navy)}
.main-nav{left:501px;top:36px;display:flex;gap:19px;font-family:"Nunito Sans",sans-serif;font-size:12px;color:#777}
.main-nav .active{color:var(--navy)}
.search-btn{left:844px;top:31px;width:27px;height:27px;background:#d3d3d3}

.hero{left:0;top:78px;width:979px;height:352px;background:linear-gradient(180deg,#e9dccb 0%,#cdb293 35%,#8a5c40 68%,#3e3630 100%)}
.hero-arrow{top:239px;width:32px;height:32px;border-radius:50%;background:var(--white);box-shadow:0 1px 4px rgba(0,0,0,.35)}
.hero-caption{left:171px;top:304px;width:637px;height:94px;background:rgba(40,40,40,.6);padding:12px 22px}
.hero-title{font-size:20px;font-weight:600;color:var(--blue-bright);letter-spacing:.3px}
.hero-text{margin-top:6px;font-size:10.8px;line-height:18px;color:var(--white)}

.section-title{width:979px;text-align:center;font-family:"Nunito Sans",sans-serif;font-size:17px;color:var(--heading)}
.section-title span{color:var(--blue)}
.welcome-text{left:120px;top:518px;width:739px;text-align:center;font-size:10.5px;line-height:20.5px}

.services-band{left:0;top:616px;width:979px;height:290px;background:var(--band)}
.pager{display:flex;gap:4px}
.service{top:698px;width:180px}
.service-photo{height:113px;border-radius:3px}
.service-text{margin-top:24px;padding-left:2px;font-size:10.5px;line-height:18.5px}

.post{top:1005px;width:260px;display:flex;gap:14px}
.post-date{width:49px;height:47px;background:var(--date);color:var(--white);text-align:center;flex:none;padding-top:5px}
.post-date b{display:block;font-weight:400;font-size:17px;line-height:19px}
.post-date small{font-size:10px}
.post-text{font-size:10.5px;line-height:18px;margin-top:-1px}
.post-more{display:block;margin-top:3px;font-style:italic;color:#333}

.site-footer{left:0;top:1125px;width:979px;height:75px;background:var(--footer)}
.copyright{left:137px;top:1158px;font-size:10.5px;color:#ddd}
.badge{top:1146px;height:38px;background:var(--white)}
.social{top:1150px;width:30px;height:30px;border-radius:50%;border:2px solid #888;background:#555}
</style>
</head>
<body>
<header class="site-header abs">
  <div class="brand abs"><span class="brand-mark"></span><span class="brand-name">Lorn Systems</span></div>
  <nav class="main-nav abs"><span class="active">Home</span><span>About</span><span>Services</span><span>Blog</span><span>Order</span><span>Contact us</span></nav>
  <div class="search-btn abs">
    <svg width="27" height="27" viewBox="0 0 27 27"><circle cx="12.5" cy="12.5" r="3.5" fill="none" stroke="#777" stroke-width="1.5"/><line x1="15" y1="15" x2="18" y2="18" stroke="#777" stroke-width="1.5"/></svg>
  </div>
</header>

<section class="hero abs" role="img" aria-label="City skyline of high-rise office towers at sunset"></section>
<div class="hero-arrow abs" style="left:90px">
  <svg width="32" height="32" viewBox="0 0 32 32"><polyline points="19,10 13,16 19,22" fill="none" stroke="#333" stroke-width="3"/></svg>
</div>
<div class="hero-arrow abs" style="left:858px">
  <svg width="32" height="32" viewBox="0 0 32 32"><polyline points="13,10 19,16 13,22" fill="none" stroke="#333" stroke-width="3"/></svg>
</div>
<div class="hero-caption abs">
  <h1 class="hero-title">NEQUE PORRO QUISQUAM</h1>
  <p class="hero-text">Lorem ipsum dolor sit amet, consectetur adipisicing elit, sed do eiusmod tempor incididunt ut labore et dolore magna aliqua.<br>Ut enim ad minim veniam, quis nostrud exercitation ullamco laboris nisi ut aliquip ex ea commodo consequat.</p>
</div>

<h2 class="section-title abs" style="left:0;top:479px">Welcome to Our Website <span>Mainpage..</span></h2>
<p class="welcome-text abs">Lorem ipsum dolor sit amet, consectetur adipisicing elit, sed do eiusmod tempor incididunt ut labore et dolore magna aliqua. Ut enim ad minim veniam quis nostrud exercitation ullamco laboris nisi ut aliquip ex ea commodo consequat. Duis aute irure dolor in reprehenderit in voluptate velit<br>Duis aute irure dolor esse cillum dolore eu fugiat nulla pariatur.</p>

<section class="services-band abs"></section>
<h2 class="section-title abs" style="left:0;top:652px">View Our <span>Services</span></h2>
<div class="pager abs" style="left:840px;top:658px">
  <svg width="30" height="14" viewBox="0 0 30 14"><circle cx="6.5" cy="7" r="5.5" fill="none" stroke="#555"/><polyline points="7.5,4.5 5,7 7.5,9.5" fill="none" stroke="#555"/><line x1="5" y1="7" x2="9.5" y2="7" stroke="#555"/><circle cx="23.5" cy="7" r="5.5" fill="none" stroke="#aaa"/><polyline points="22.5,4.5 25,7 22.5,9.5" fill="none" stroke="#aaa"/><line x1="20.5" y1="7" x2="25" y2="7" stroke="#aaa"/></svg>
</div>
<div class="service abs" style="left:106px"><div class="service-photo" role="img" aria-label="Rope access technician in helmet working at height" style="background:linear-gradient(135deg,#d8d6d2,#6b6762 55%,#2f2c2a)"></div><p class="service-text">Excepteur sint occaecat cupidataest non proident, sunt dolore.</p></div>
<div class="service abs" style="left:302px"><div class="service-photo" role="img" aria-label="Tower cranes over a building under construction" style="background:linear-gradient(180deg,#7d9cc9,#b9bccb 55%,#6e5c58)"></div><p class="service-text">Excepteur sint occaecat cupidataest non proident, sunt dolore.</p></div>
<div class="service abs" style="left:498px"><div class="service-photo" role="img" aria-label="Two engineers in hard hats reviewing plans at a steel frame site" style="background:linear-gradient(180deg,#2e64b8,#5f8fcf 55%,#c7773a)"></div><p class="service-text">Excepteur sint occaecat cupidataest non proident, sunt dolore.</p></div>
<div class="service abs" style="left:694px"><div class="service-photo" role="img" aria-label="Yellow hard hat held beside a tool belt" style="background:linear-gradient(135deg,#f1efea,#e7c34a 50%,#5f6f8c)"></div><p class="service-text">Excepteur sint occaecat cupidataest non proident, sunt dolore.</p></div>

<h2 class="section-title abs" style="left:0;top:955px">Recent <span>Blog Post</span></h2>
<div class="pager abs" style="left:841px;top:957px">
  <svg width="30" height="14" viewBox="0 0 30 14"><circle cx="6.5" cy="7" r="5.5" fill="none" stroke="#555"/><polyline points="7.5,4.5 5,7 7.5,9.5" fill="none" stroke="#555"/><line x1="5" y1="7" x2="9.5" y2="7" stroke="#555"/><circle cx="23.5" cy="7" r="5.5" fill="none" stroke="#aaa"/><polyline points="22.5,4.5 25,7 22.5,9.5" fill="none" stroke="#aaa"/><line x1="20.5" y1="7" x2="25" y2="7" stroke="#aaa"/></svg>
</div>
<article class="post abs" style="left:110px"><div class="post-date"><b>02</b><small>JUNE</small></div><p class="post-text">Ut enim ad minim veniam, quis nostrud exe rcitation ullamco lab eris nisi ut aliquip<span class="post-more">Read More..</span></p></article>
<article class="post abs" style="left:380px"><div class="post-date"><b>02</b><small>JUNE</small></div><p class="post-text">Ut enim ad minim veniam, quis nostrud exe rcitation ullamco lab eris nisi ut aliquip<span class="post-more">Read More..</span></p></article>
<article class="post abs" style="left:650px"><div class="post-date"><b>02</b><small>JUNE</small></div><p class="post-text">Ut enim ad minim veniam, quis nostrud exe rcitation ullamco lab eris nisi ut aliquip<span class="post-more">Read More..</span></p></article>

<footer class="site-footer abs"></footer>
<p class="copyright abs">Copyright ©2014 Yoursite All Rights Reserved.</p>
<div class="badge abs" style="left:575px;width:59px"></div>
<div class="badge abs" style="left:652px;width:73px"></div>
<div class="social abs" style="left:762px"></div>
<div class="social abs" style="left:801px"></div>
<div class="social abs" style="left:840px"></div>
</body>
</html>
```